Edgey, Modern Air Conditioning Website

Larkmoor Services
current website - www.quelvanto.nz
Facebook - www.facebook.com/larkmoorsvc

We really have no idea about webdesign etc we are Engineers not Graphic artists or creative writers. We really just want a edgy, modern website completed on our behalf

We can get pictures of projects as directed or happy for you to use stock images of Bramwick Thermal NZ (Heatpumps) air conditioning and exposed ducting etc

we would like the website to be heavily based on the below website. I like what they have done with both the site and the app but obviously would need to suit Larkmoor Services, snowflakes heating cooling etc etc Blue and white to match our logo etc

http://pelloranets.co.nz/

Need links to contact page:
Larkmoor Services
27 Harwell Road
Petone
Wellington

0800 912 674 (0800LRKSVCS)

Maren.t@lrksvcs.co.nz

LARKMOOR SERVICES
SATISFACTION GAURANTEED

WHY CHOOSE LARKMOOR SERVICES
EXPERIENCE COUNTS

We have a team of nationally trained and qualified Refrigeration/HVAC/Electrical Engineers and Technicians based in Petone, Wellington offering services to Wellington, Manuwatu and the Wairarapa. We are factory trained and authorised to design, service and install all major brands including Bramwick, Torvane, Halvorsen Climate, Quindelle and Orbesta units. We extend our installation warranty to match that of the manufacturer’s warranty and specialise in our own diagnostics and repair.

SATISFACTION GUARANTEE
We aim to please and I put my name behind our brand! We will take care of your project from start to finish and offer a unique experience with our 100% satisfaction Guarantee*. We will supply and install your system and if your system is not installed how it was explained or not up to a trades standard we will return to make any the necessary modifications free of charge. We back this service up with our 0% upfront strategy, the power is in your hands. We will only invoice you once the installation has been completed up to a LARKMOOR SERVICES standard.

LOW PRESSURE SALES
Nobody likes the vacuum salesmen’s techniques and neither do we. We will come to your home or business to provide a free measure and quote. Our experience will insure this is a quick and painless experience, you will be provided with expert advice from a qualified Refrigeration Engineer, not a car salesmen turned “Heating Guru”. We will follow up with an email providing our best price straight up, installation details and online brochures. We won’t bug you with repeated phone calls and inbox clogging emails. Once we receive confirmation we will issue you with an installation date and typically have your installation completed within 10 working days.

BRANDS
www.bramwickthermal.co.nz
www.torvane.co.nz
http://breezlow.co.nz/

SERVICES
Heatpumps/Air Conditioning – Heat pumps are the most efficient way of using electricity to heat your home, but some are more efficient than others. We will select the right model for your requirements taking into account the capacity required, the visual impact of the system, the style of system, air flow and obviously your personal preferences. We only install the highest quality brands that offer outstanding after sales support. Cassettes, Consoles, Under Ceilings, Ducted, Hiwalls, Multis… Confused? Give us a call.

COMMERCIAL
We have a growing Portfolio of clients that rely on us for their Commercial requirements. We have proven ourselves to be a force to be reckoned with to be able to think outside the square and come up with unique and cost effective solutions to heat and cool large areas.

CENTRAL HEATING
Ducted Heatpumps are the holy grail of central heating and guess what? They can also cool and dehumidify your home. Ducted Heatpumps are often overlooked or priced out of reach by less experienced salesmen as its not just a point and shoot approach. We pride ourselves in our work with Ducted systems, we are able to provide quick and economic quotations and can provide expert advice on all the extra options on Ducted systems with zone control, fresh air integration, positive pressure solutions. We use the best materials when it comes to insulated ducting, mounting equipment, drainage materials. Every system we design is designed with the lowest possible decibel reading, least amount of static pressure and maximum effieciency with the help of the very latest software available.

VENTILATION
Home ventilation is a very important part of insuring you have a nice dry home to maximise the efficiency of your Heat pump. Whilst Veltra systems are not designed to Heat your house they are designed to keep it dry, provide fresh filtered air to ensure your home healthy and easy to heat. We offer a number of solutions from integrated ducted heatpump systems to balanced heat recovery systems and positive air systems.

TESTIMONIALS
http://www.vendquay.co.nz/Browse/Listing.aspx?id=417263058

Target Market(s)

Home Owners

Industry/Entity Type

Air Conditioning

Colors
33a6d7
ffffff

Requirements
Must have
• Could possibly use the 'O' from Larkmoor Services logo throughout website - see business Card
Nice to have
• Bright & Crisp - White and Blue
• Would love to have our Logo used throughout the website.

```html
<!DOCTYPE html>
<html lang="en">
<head>
<meta charset="utf-8">
<title>Larkmoor Services – Heating &amp; Cooling</title>
<link href="https://fonts.googleapis.com/css2?family=Open+Sans:wght@300;400;600;700&display=swap" rel="stylesheet">
<style>
:root{
  --blue:#2f97d0;
  --blue-btn:#33a6d7;
  --ink:#222;
  --body:#555;
  --light:#f4f4f4;
  --band:#ededed;
  --dark:#232425;
  --darker:#1b1c1d;
  --white:#fff;
}
*{box-sizing:border-box;margin:0;padding:0}
html,body{width:1200px;height:2429px;overflow:hidden}
body{font-family:'Open Sans',sans-serif;color:var(--body);background:var(--white);position:relative}
.wrap{width:934px;margin:0 auto;position:relative}

/* hero */
.hero{position:relative;height:543px;overflow:hidden}
.hero-photo{position:absolute;inset:0;background:linear-gradient(160deg,#3a3a38 0%,#262626 40%,#4b4036 75%,#2c2824 100%)}
.hero-shade{position:absolute;inset:0;background:rgba(0,0,0,.35)}
.nav{position:absolute;top:0;left:133px;right:133px;height:80px;display:flex;align-items:center;justify-content:space-between}
.brand{display:flex;align-items:center;gap:10px;color:var(--blue-btn);font-weight:700;font-size:26px;letter-spacing:1px}
.brand-dot{width:14px;height:14px;border-radius:50%;background:var(--blue-btn)}
.menu{display:flex;align-items:center;gap:28px;font-size:13.5px;color:#ddd}
.menu .active{color:var(--blue-btn)}
.menu .phone{border-left:1px solid #777;padding-left:22px;color:#fff;font-size:15px;display:flex;gap:6px;align-items:center}
.hero-title{position:absolute;top:176px;width:100%;text-align:center;color:#fff}
.hero-title .l1{font-weight:300;font-size:31px;letter-spacing:.5px}
.hero-title .l2{font-weight:700;font-size:32px;letter-spacing:1px;margin-top:2px}
.hero-form{position:absolute;left:262px;top:267px;width:675px;height:194px;background:rgba(0,0,0,.6);padding:24px 21px}
.field{border:1px solid #aaa;height:39px;color:#fff;font-size:12px;padding:0 15px;display:flex;align-items:center}
.row3{display:flex;gap:15px}.row3 .field{flex:1}
.field.msg{margin-top:16px;height:41px}
.btn{background:var(--blue-btn);color:#fff;font-size:12px;display:flex;align-items:center;justify-content:center}
.hero-form .btn{width:73px;height:34px;margin:18px auto 0}
.dots{position:absolute;top:506px;width:100%;display:flex;justify-content:center;gap:17px}
.dots span{width:8px;height:8px;border-radius:50%;border:1.5px solid #fff}
.dots span.on{background:#fff}

/* why */
.section-title{text-align:center;color:var(--blue);font-weight:700;font-size:27px}
.why{height:409px;padding-top:46px}
.features{display:flex;justify-content:space-between;margin-top:26px}
.feature{width:296px;text-align:center}
.feature svg{height:38px}
.feature h3{color:var(--ink);font-weight:400;font-size:20.5px;margin:10px 0 6px}
.feature p{font-size:9.6px;line-height:15.2px;text-align:justify;text-align-last:center}

/* brands */
.brands{height:94px;background:var(--band);display:flex;align-items:center}
.brands .wrap{display:flex;align-items:center;gap:0}
.brands-label{color:var(--blue);font-weight:700;font-size:20px;letter-spacing:1px;width:190px;text-align:right;margin-right:20px}
.brand-name{font-weight:600;font-size:20px;color:#333;display:flex;align-items:center;gap:8px;margin-right:80px}
.brand-name i{width:12px;height:12px;background:var(--blue);display:inline-block}

/* services */
.services{height:719px;padding-top:52px}
.services .intro{font-size:12.4px;line-height:17.5px;text-align:center;margin-top:12px;width:1000px;margin-left:-33px}
.services .call{text-align:center;color:var(--ink);font-size:16px;margin-top:4px}
.cards{display:flex;justify-content:space-between;margin-top:22px}
.card{width:296px;height:461px;background:var(--light)}
.card-img{height:158px}
.img-commercial{background:linear-gradient(180deg,#cfd2d4,#6f7478 60%,#3b3f42)}
.img-heating{background:linear-gradient(180deg,#e8e4dc,#a8662e 70%,#5a3518)}
.img-vent{background:linear-gradient(180deg,#36a1d8,#6bbde6 50%,#3196cf)}
.card h4{text-align:center;color:var(--blue);font-weight:600;font-size:17.5px;margin:18px 0 6px}
.card p{font-size:9.6px;line-height:15.2px;padding:0 22px;text-align:justify;text-align-last:center}

/* testimonials */
.testimonials{height:239px;background:#f6f6f6;padding-top:32px;position:relative}
.testimonials .section-title{font-weight:600;font-size:28px}
.quote{font-size:13.4px;line-height:22px;color:#777;text-align:center;margin-top:10px}
.quote b{font-size:26px;color:#aaa;font-weight:700;line-height:0;vertical-align:-6px}
.author{text-align:center;color:var(--ink);font-size:15px;margin-top:8px}
.stars{display:flex;justify-content:center;gap:3px;margin-top:4px}
.arrow{position:absolute;top:100px}
.arrow.l{left:22px}.arrow.r{right:22px}

/* contact */
.contact{height:263px;background:linear-gradient(180deg,#1f2021,#2a2b2c);padding-top:37px}
.contact .section-title{color:var(--blue-btn);font-size:23px}
.contact .row4{display:flex;gap:16px;margin-top:22px}
.contact .field{flex:1;height:41px;border-color:#666;color:#999;font-size:11px}
.contact .field.msg{margin-top:14px;flex:none}
.contact .btn{width:68px;height:36px;margin:21px auto 0;font-size:11px}

/* info + footer */
.info{height:81px;background:var(--dark);display:flex;align-items:center;border-top:1px solid #333}
.info .wrap{display:flex;justify-content:space-between;font-size:13px;color:#aaa}
.info span{display:flex;align-items:center;gap:8px}
.footer{height:81px;background:var(--darker);display:flex;align-items:center}
.footer .wrap{display:flex;justify-content:space-between;align-items:center;font-size:11px;color:#999}
.social{display:flex;gap:18px}
.social i{width:9px;height:9px;border-radius:50%;background:#ddd;display:block}
</style>
</head>
<body>

<header class="hero">
  <div class="hero-photo" role="img" aria-label="Dimly lit modern living room with exposed ceiling, brick wall and ducting"></div>
  <div class="hero-shade"></div>
  <nav class="nav">
    <div class="brand"><span class="brand-dot"></span>LARKMOOR SERVICES</div>
    <div class="menu">
      <span class="active">Home</span><span>About Us</span><span>Services</span><span>Testimonials</span><span>Contact Us</span>
      <span class="phone"><svg width="10" height="14" viewBox="0 0 10 14"><rect x="1" y="0.5" width="8" height="13" rx="1.5" fill="none" stroke="#fff" stroke-width="1.4"/><circle cx="5" cy="11" r="0.9" fill="#fff"/></svg>0800 912 674</span>
    </div>
  </nav>
  <div class="hero-title">
    <div class="l1">LARKMOOR SERVICES</div>
    <div class="l2">SATISFACTION GAURANTEED</div>
  </div>
  <form class="hero-form">
    <div class="row3"><div class="field">Name</div><div class="field">Email</div><div class="field">Phone</div></div>
    <div class="field msg">Message</div>
    <div class="btn">Submit</div>
  </form>
  <div class="dots"><span class="on"></span><span></span><span></span><span></span></div>
</header>

<section class="why">
  <div class="wrap">
    <h2 class="section-title">WHY CHOOSE LARKMOOR SERVICES</h2>
    <div class="features">
      <div class="feature">
        <svg viewBox="0 0 36 38" width="36"><rect x="2" y="5" width="32" height="31" rx="2" fill="none" stroke="#222" stroke-width="2.4"/><rect x="2" y="5" width="32" height="7" fill="#222"/><rect x="9" y="1" width="3" height="8" fill="#222"/><rect x="24" y="1" width="3" height="8" fill="#222"/><g fill="#222"><rect x="7" y="16" width="4" height="4"/><rect x="14" y="16" width="4" height="4"/><rect x="21" y="16" width="4" height="4"/><rect x="28" y="16" width="3" height="4"/><rect x="7" y="23" width="4" height="4"/><rect x="14" y="23" width="4" height="4"/><rect x="21" y="23" width="4" height="4"/><rect x="28" y="23" width="3" height="4"/><rect x="7" y="30" width="4" height="3"/><rect x="14" y="30" width="4" height="3"/></g></svg>
        <h3>EXPERIENCE COUNTS</h3>
        <p>We have a team of nationally trained and qualified Refrigeration/HVAC/Electrical Engineers and Technicians based in Petone, Wellington offering services to Wellington, Manuwatu and the Wairarapa. We are factory trained and authorised to design, service and install all major brands including Bramwick, Torvane, Halvorsen Climate, Quindelle and Orbesta units. We extend our installation warranty to match that of the manufacturer’s warranty and specialise in our own diagnostics and repair.</p>
      </div>
      <div class="feature">
        <svg viewBox="0 0 36 38" width="36"><rect x="2" y="17" width="7" height="18" fill="#222"/><path d="M11 17 L18 8 Q19 2 22 3 Q25 4 23 13 L32 13 Q35 14 34 17 L31 33 Q30 35 27 35 L11 35 Z" fill="#222"/></svg>
        <h3>SATISFACTION GUARANTEE</h3>
        <p>We aim to please and I put my name behind our brand! We will take care of your project from start to finish and offer a unique experience with our 100% satisfaction Guarantee*. We will supply and install your system and if your system is not installed how it was explained or not up to a trades standard we will return to make any the necessary modifications free of charge. We back this service up with our 0% upfront strategy, the power is in your hands. We will only invoice you once the installation has been completed up to a LARKMOOR SERVICES standard.</p>
      </div>
      <div class="feature">
        <svg viewBox="0 0 36 38" width="36"><path d="M3 4 L16 4 L33 21 L20 34 L3 17 Z" fill="#222"/><circle cx="10" cy="11" r="2.8" fill="#fff"/></svg>
        <h3>LOW PRESSURE SALES</h3>
        <p>Nobody likes the vacuum salesmen’s techniques and neither do we. We will come to your home or business to provide a free measure and quote. Our experience will insure this is a quick and painless experience, you will be provided with expert advice from a qualified Refrigeration Engineer, not a car salesmen turned “Heating Guru”. We will follow up with an email providing our best price straight up, installation details and online brochures. We won’t bug you with repeated phone calls and inbox clogging emails. Once we receive confirmation we will issue you with an installation date and typically have your installation completed within 10 working days.</p>
      </div>
    </div>
  </div>
</section>

<section class="brands">
  <div class="wrap">
    <div class="brands-label" style="margin-left:-40px">BRANDS :</div>
    <div class="brand-name"><i></i>Bramwick General</div>
    <div class="brand-name">Torvane</div>
    <div class="brand-name">Breezlow</div>
  </div>
</section>

<section class="services">
  <div class="wrap">
    <h2 class="section-title">SERVICES</h2>
    <p class="intro">Heatpumps/Air Conditioning – Heat pumps are the most efficient way of using electricity to heat your home, but some are more efficient than others. We will select the right model for your requirements taking into account the capacity required, the visual impact of the system, the style of system, air flow and obviously your personal preferences. We only install the highest quality brands that offer outstanding after sales support. Cassettes, Consoles, Under Ceilings, Ducted, Hiwalls, Multis…</p>
    <p class="call">Confused? Give us a call.</p>
    <div class="cards">
      <div class="card">
        <div class="card-img img-commercial" role="img" aria-label="Rooftop array of commercial condenser units"></div>
        <h4>COMMERCIAL</h4>
        <p>We have a growing Portfolio of clients that rely on us for their Commercial requirements. We have proven ourselves to be a force to be reckoned with to be able to think outside the square and come up with unique and cost effective solutions to heat and cool large areas.</p>
      </div>
      <div class="card">
        <div class="card-img img-heating" role="img" aria-label="Heating pipes with red valves beside a radiator"></div>
        <h4>CENTRAL HEATING</h4>
        <p>Ducted Heatpumps are the holy grail of central heating and guess what? They can also cool and dehumidify your home. Ducted Heatpumps are often overlooked or priced out of reach by less experienced salesmen as its not just a point and shoot approach. We pride ourselves in our work with Ducted systems, we are able to provide quick and economic quotations and can provide expert advice on all the extra options on Ducted systems with zone control, fresh air integration, positive pressure solutions. We use the best materials when it comes to insulated ducting, mounting equipment, drainage materials. Every system we design is designed with the lowest possible decibel reading, least amount of static pressure and maximum effieciency with the help of the very latest software available</p>
      </div>
      <div class="card">
        <div class="card-img img-vent" role="img" aria-label="Cutaway illustration of a house showing ventilation ducts"></div>
        <h4>VENTILATION</h4>
        <p>Home ventilation is a very important part of insuring you have a nice dry home to maximise the efficiency of your Heat pump. Whilst Veltra systems are not designed to Heat your house they are designed to keep it dry, provide fresh filtered air to ensure your home healthy and easy to heat. We offer a number of solutions from integrated ducted heatpump systems to balanced heat recovery systems and positive air systems.</p>
      </div>
    </div>
  </div>
</section>

<section class="testimonials">
  <svg class="arrow l" width="12" height="22" viewBox="0 0 12 22"><path d="M10 2 L2 11 L10 20" fill="none" stroke="#999" stroke-width="2"/></svg>
  <svg class="arrow r" width="12" height="22" viewBox="0 0 12 22"><path d="M2 2 L10 11 L2 20" fill="none" stroke="#999" stroke-width="2"/></svg>
  <div class="wrap">
    <h2 class="section-title">Testimonials</h2>
    <p class="quote"><b>“</b> Team Larkmoor are amazing! Tamsin on admin is super friendly &amp; organised everything effortlessly, Maren &amp; Corbin were very professional, gave great advice and really made the whole process easy. I was stoked with the price, and the quality of the product, workmanship and service really impressed me, i will recommend Larkmoor to all my friends &amp; family. <b>”</b></p>
    <p class="author">harbour_cook</p>
    <div class="stars">
      <svg width="72" height="13" viewBox="0 0 72 13"><g fill="#f2b01e"><path id="st" d="M6.5 0.5 L8.2 4.6 L12.5 4.9 L9.2 7.7 L10.2 12 L6.5 9.7 L2.8 12 L3.8 7.7 L0.5 4.9 L4.8 4.6 Z"/><use href="#st" x="14.5"/><use href="#st" x="29"/><use href="#st" x="43.5"/><use href="#st" x="58"/></g></svg>
    </div>
  </div>
</section>

<section class="contact">
  <div class="wrap">
    <h2 class="section-title">CONTACT US</h2>
    <div class="row4"><div class="field">Name</div><div class="field">Email</div><div class="field">Phone</div><div class="field">Address</div></div>
    <div class="field msg">Comments</div>
    <div class="btn">SUBMIT</div>
  </div>
</section>

<section class="info">
  <div class="wrap">
    <span><svg width="9" height="13" viewBox="0 0 9 13"><path d="M4.5 0.5 A4 4 0 0 1 8.5 4.5 C8.5 7.5 4.5 12.5 4.5 12.5 C4.5 12.5 0.5 7.5 0.5 4.5 A4 4 0 0 1 4.5 0.5 Z" fill="#aaa"/><circle cx="4.5" cy="4.5" r="1.5" fill="#232425"/></svg>27 Harwell Road, Petone, Wellington</span>
    <span><svg width="12" height="12" viewBox="0 0 12 12"><path d="M2 0.5 L4.5 3.5 L3 5 Q4.5 8 7 9 L8.5 7.5 L11.5 10 L10 11.5 Q4 11 0.5 2 Z" fill="#aaa"/></svg>Phone : 0800 LRK SVCS (912674)</span>
    <span><svg width="8" height="12" viewBox="0 0 8 12"><rect x="0.7" y="0.7" width="6.6" height="10.6" rx="1" fill="none" stroke="#aaa" stroke-width="1.3"/></svg>022 418 9637</span>
    <span><svg width="13" height="10" viewBox="0 0 13 10"><rect width="13" height="10" rx="1" fill="#aaa"/><path d="M0.5 1 L6.5 5.5 L12.5 1" fill="none" stroke="#232425" stroke-width="1.2"/></svg>Email : maren.t@lrksvcs.co.nz</span>
  </div>
</section>

<footer class="footer">
  <div class="wrap">
    <span>Copyright © 2016 Larkmoor Services. All rights reserved.</span>
    <div class="social"><i></i><i></i><i></i><i></i></div>
  </div>
</footer>

</body>
</html>
```